Retractable Banner Stands

Hello we need a deisgn for a banner.
Sizes: 36"x80", 12"x17"(this one to have less on it, most the logo, license numvber, and address), and a 24"x40" banner
Roofing Services
HOA & Commercial Roofing
• Emergency roof tarping & repairs — Starting at $550
• Small & large roof repairs
• Preventative roof maintenance
• Full roof replacement
Deck & Balcony Services
• Balcony & deck maintenance
SB-326 Repairs
• Deck resurfacing
• Small & large deck repairs
• Full deck reconstruction
Gutter Services
• Small & large gutter repairs
• Gutter cleaning & maintenance
• New gutter installation & replacement
License Information:
C-39 Roofing Contractor
General B Contractor
License #4529730
📍 Serving Orange County & Surrounding Areas
📍 Office Location:
41 Dunwick Street, Suite F
Target Market(s)
HOA & Commerical roofs
Industry/Entity Type
Roofing
Other font styles liked:
- Gotham
Look and feel

```html
<!DOCTYPE html>
<html lang="en">
<head>
<meta charset="utf-8">
<title>Keystone Roofing & Waterproofing — Roofing Services Banner</title>
<link href="https://fonts.googleapis.com/css2?family=Montserrat:wght@500;600;700;800;900&display=swap" rel="stylesheet">
<style>
  :root{
    --blue:#1fa6e0;
    --blue-dark:#0b7fb8;
    --ink:#111418;
    --ink-soft:#23272d;
    --pale:#e8f3f9;
    --grey:#d9dde1;
    --white:#ffffff;
    --roof-top:#6e5a49;
    --roof-mid:#b7c0c6;
  }
  *{box-sizing:border-box;margin:0;padding:0}
  html,body{width:789px;height:1200px;overflow:hidden;background:#f2f3f4}
  body{font-family:"Montserrat",Arial,sans-serif;color:var(--ink)}
  .banner{position:relative;width:789px;height:1200px;background:var(--white);overflow:hidden}

  .hero-photo{position:absolute;left:0;top:0;width:789px;height:400px;
    background:linear-gradient(160deg,#8a6a4c 0%,#6f6a63 30%,var(--roof-mid) 60%,#8d98a0 100%)}
  .hero-roof{position:absolute;left:0;top:290px;width:789px;height:150px}
  .brand{position:absolute;left:0;top:338px;width:789px;text-align:center;color:var(--white);
    font-weight:800;font-size:24px;letter-spacing:1px;line-height:1.1}
  .brand small{display:block;font-size:11px;letter-spacing:2.5px;margin-top:4px;font-weight:800}

  .headline{position:absolute;left:0;top:430px;width:789px;height:82px;background:var(--ink);
    color:var(--white);text-align:center;font-weight:900;font-size:64px;line-height:82px;letter-spacing:1px}
  .subline-band{position:absolute;left:0;top:512px;width:789px;height:58px;background:var(--pale)}
  .subline{position:absolute;left:80px;top:522px;width:629px;height:44px;background:var(--blue);
    color:var(--white);text-align:center;font-weight:800;font-size:28px;line-height:44px}

  .services{position:absolute;left:0;top:570px;width:789px;height:215px;background:var(--pale);
    display:grid;grid-template-columns:1fr 1fr;gap:22px 30px;padding:22px 50px}
  .service{display:flex;align-items:center;gap:16px;font-weight:600;font-size:19px;line-height:1.25}
  .service svg{flex:0 0 58px;width:58px;height:64px}

  .section-label{position:absolute;height:40px;color:var(--white);font-weight:800;font-size:19px;
    line-height:40px;padding-left:28px}
  .deck-label{left:0;top:795px;width:410px;background:var(--blue)}
  .deck-list{position:absolute;left:36px;top:845px;width:380px;list-style:none;
    font-weight:700;font-size:17px;line-height:1.35}
  .deck-list li{position:relative;padding-left:22px;margin-bottom:4px}
  .deck-list li::before{content:"";position:absolute;left:2px;top:8px;width:9px;height:9px;border-radius:50%;background:var(--blue)}
  .deck-photo{position:absolute;left:430px;top:795px;width:330px;height:165px;
    background:linear-gradient(135deg,#4b4f53 0%,#9aa2a8 50%,#5d6368 100%)}

  .gutter-label{left:0;top:975px;width:230px;background:var(--ink)}
  .gutter-cols{position:absolute;left:30px;top:1020px;width:729px;height:80px;display:grid;
    grid-template-columns:repeat(3,1fr)}
  .gutter-cols div{padding:12px 18px;font-weight:600;font-size:16px;line-height:1.3}
  .gutter-cols div:nth-child(1){background:var(--grey)}
  .gutter-cols div:nth-child(2){background:#e7e9eb}
  .gutter-cols div:nth-child(3){background:var(--white);border:1px solid var(--grey)}

  .license{position:absolute;left:0;top:1112px;width:789px;height:42px;background:var(--ink);
    color:var(--white);text-align:center;font-weight:800;font-size:17px;line-height:42px;letter-spacing:.5px}
  .license span{color:var(--blue)}
  .locale{position:absolute;left:0;top:1154px;width:789px;height:46px;background:var(--pale);
    display:flex;align-items:center;justify-content:center;gap:10px;font-weight:600;font-size:15px}
  .locale svg{width:16px;height:20px}
  .locale .divider{color:var(--blue-dark)}
</style>
</head>
<body>
<main class="banner">
  <div class="hero-photo" role="img" aria-label="Aerial photo of a commercial roof being resurfaced at sunset"></div>
  <svg class="hero-roof" viewBox="0 0 789 150" preserveAspectRatio="none" aria-hidden="true">
    <polygon points="0,150 0,110 394,20 789,110 789,150" fill="var(--ink)"/>
    <polyline points="0,108 394,18 789,108" fill="none" stroke="var(--blue)" stroke-width="6"/>
    <polyline points="0,96 394,4 789,96" fill="none" stroke="var(--white)" stroke-width="4"/>
  </svg>
  <div class="brand">KEYSTONE<small>ROOFING &amp; WATERPROOFING</small></div>

  <h1 class="headline">ROOFING SERVICES</h1>
  <div class="subline-band"></div>
  <h2 class="subline">HOA &amp; Commercial Roofing</h2>

  <section class="services">
    <div class="service">
      <svg viewBox="0 0 58 64" aria-hidden="true"><polygon points="29,2 55,17 55,47 29,62 3,47 3,17" fill="var(--white)" stroke="var(--ink)" stroke-width="3"/><path d="M16 36 L29 24 L42 36 M20 34 V44 H38 V34" fill="none" stroke="var(--blue)" stroke-width="3.5"/></svg>
      <span>Emergency Roof Tarping &amp; Repairs — Starting at $550</span>
    </div>
    <div class="service">
      <svg viewBox="0 0 58 64" aria-hidden="true"><polygon points="29,2 55,17 55,47 29,62 3,47 3,17" fill="var(--white)" stroke="var(--ink)" stroke-width="3"/><path d="M14 38 L29 24 L44 38" fill="none" stroke="var(--ink)" stroke-width="4"/><path d="M19 38 V46 H39 V38" fill="none" stroke="var(--blue)" stroke-width="3.5"/></svg>
      <span>Full Roof Replacement</span>
    </div>
    <div class="service">
      <svg viewBox="0 0 58 64" aria-hidden="true"><polygon points="29,2 55,17 55,47 29,62 3,47 3,17" fill="var(--white)" stroke="var(--ink)" stroke-width="3"/><path d="M18 44 L36 26 M33 20 L42 29" stroke="var(--blue)" stroke-width="5" stroke-linecap="round"/></svg>
      <span>Small &amp; Large Roof Repairs</span>
    </div>
    <div class="service">
      <svg viewBox="0 0 58 64" aria-hidden="true"><polygon points="29,2 55,17 55,47 29,62 3,47 3,17" fill="var(--white)" stroke="var(--ink)" stroke-width="3"/><path d="M18 32 L26 40 L41 24" fill="none" stroke="var(--blue)" stroke-width="4.5" stroke-linecap="round"/></svg>
      <span>Preventative Roof Maintenance</span>
    </div>
  </section>

  <div class="section-label deck-label">Deck &amp; Balcony Services</div>
  <ul class="deck-list">
    <li>Balcony &amp; Deck Maintenance SB-326 Repairs</li>
    <li>Small &amp; large deck repairs</li>
    <li>Full Deck reconstruction</li>
    <li>Deck Resurfacing</li>
  </ul>
  <div class="deck-photo" role="img" aria-label="Photo of a worker repairing a balcony deck"></div>

  <div class="section-label gutter-label">Gutter Services</div>
  <div class="gutter-cols">
    <div>Small &amp; large gutter repairs</div>
    <div>Gutter cleaning &amp; maintenance</div>
    <div>New gutter installation &amp; replacement</div>
  </div>

  <div class="license">C-39 ROOFING CONTRACTOR GENERAL B CONTRACTOR LICENSE <span>#4529730</span></div>
  <div class="locale">
    <svg viewBox="0 0 16 20" aria-hidden="true"><path d="M8 19 C3 12 1 9 1 7 A7 7 0 0 1 15 7 C15 9 13 12 8 19Z" fill="var(--blue)"/><circle cx="8" cy="7" r="2.6" fill="var(--white)"/></svg>
    <span>Serving Orange County &amp; Surrounding Areas</span>
    <span class="divider">|</span>
    <span>41 Dunwick Street, Suite F</span>
  </div>
</main>
</body>
</html>
```